Seven Quiet Rooms Poster

Seven Quiet Rooms is reaching out to designers, creatives and fans alike to help create an exciting new poster for the film as part of our Fundvaro campaign.

Seven Quiet Rooms is a multi-protagonist, multicultural, humanist drama inspired by the 2008 Mumbai terrorist attacks. Centering on a group of international tourists trapped in their hotel by Islamic fundamentalists, the film aims to explore the key issues facing our society, concerning atheism, religion, religious extremism and humanism.

The film’s poster will be a critical part of a film’s publicity and marketing portfolio and an important resource for the film to take into our festival campaign and distribution talks. We’re looking for a highly polished design that accurately represents the film and matches the standard of the finished film.

We will be uploading some of the best entries to our Chatterbox page for fans to vote on. If you do not wish for your design to appear on the page, please contact us.

You can find our teaser trailer on the Fundvaro link below. We’ve also provided some reference images (found here: http://lnk.example-short.net/Rk4WpZ) and also stills from the film to provide inspiration (found here: http://lnk.example-short.net/Tm8QvB) - how or if you use them is up to you.

Good luck and get designing!

http://www.fundvaro-example.com/projects/seven-quiet-rooms

Please note: Amber Tide Pictures reserves the right to select all promotional material for theatrical release.

Requirements
Must have
• Size: 27" x 40"
Should not have
• Please do not include the credit block on your designs.

```html
<!DOCTYPE html>
<html lang="en">
<head>
<meta charset="utf-8">
<title>Seven Quiet Rooms — Poster</title>
<link rel="stylesheet" href="https://fonts.googleapis.com/css2?family=Oswald:wght@600&display=swap">
<style>
  :root {
    --paper-centre: #f6f3ef;
    --paper-mid: #ebe6e0;
    --paper-edge: #cbc3b9;
    --ink-dark: #333333;
    --ink-red: #720404;
    --rifle-tone: #7a5a3a;
    --rifle-tone-dark: #3a3430;
    --blood-core: rgba(40, 2, 2, 0.95);
    --blood-mid: rgba(120, 6, 6, 0.55);
    --blood-clear: rgba(138, 8, 8, 0);
  }
  * { margin: 0; padding: 0; box-sizing: border-box; }
  html, body {
    width: 810px;
    height: 1200px;
    overflow: hidden;
  }
  .poster {
    position: relative;
    width: 810px;
    height: 1200px;
    background: radial-gradient(ellipse 70% 60% at 50% 52%, var(--paper-centre) 0%, var(--paper-mid) 55%, var(--paper-edge) 100%);
    overflow: hidden;
  }
  .title {
    font-family: "Oswald", "Arial Narrow", sans-serif;
    font-weight: 600;
    text-transform: uppercase;
  }
  .title-line {
    position: absolute;
    left: 12px;
    width: 100%;
    text-align: center;
    font-size: 162px;
    line-height: 162px;
    letter-spacing: 3px;
    color: var(--ink-dark);
  }
  .title-line--first { top: 163px; }
  .title-line--accent { top: 367px; color: var(--ink-red); }
  .title-line--last { top: 583px; }
  .rifle-art {
    position: absolute;
    left: 82px;
    top: 542px;
    width: 424px;
    height: 52px;
    border-radius: 18px 8px 8px 22px;
    background: linear-gradient(90deg, var(--rifle-tone) 0%, var(--rifle-tone-dark) 45%, var(--rifle-tone) 70%, var(--rifle-tone-dark) 100%);
  }
  .blood-splatter {
    position: absolute;
    left: 486px;
    top: 440px;
    width: 310px;
    height: 200px;
    background:
      radial-gradient(closest-side at 28% 56%, var(--blood-core) 0%, var(--blood-core) 45%, var(--blood-mid) 75%, var(--blood-clear) 100%),
      radial-gradient(closest-side at 50% 50%, rgba(138, 8, 8, 0.28) 0%, var(--blood-clear) 100%);
  }
</style>
</head>
<body>
  <main class="poster">
    <h1 class="title">
      <span class="title-line title-line--first">Seven</span>
      <span class="title-line title-line--accent">Quiet</span>
      <span class="title-line title-line--last">Rooms</span>
    </h1>
    <div class="rifle-art" role="img" aria-label="Illustration of an assault rifle with a wooden stock, pointing right"></div>
    <div class="blood-splatter" role="img" aria-label="Dark blood splatter bursting from the rifle's muzzle with scattered droplets"></div>
  </main>
</body>
</html>
```